Fresh & Clean *NEW* BUSINESS CARD Needed - OPTOMETRY Clinic/Optical

High-tech optometry practice with 3 doctors seeking new business card.  We provide eye exams, sell, designer glasses/contacts/specialty eyewear and treat ocular diseases.  For our business cards, we are seeking fresh, clean, and crisp design as we grow our team (staffing change).  Simply adding doctors is making the card look busy/cluttered.
 Looking for professional, less cluttered look yet still have our logo, doctor names, phone, address, and website....If possible!  :)
Names:
Marcia Trelford, O.D.
Ned Pallister, O.D.
Oona Ferrant, O.D.
Phone: 555-014-2738
Website: www.BrightLensHub.example
Address:  417 Garnet R. Holloway, Harlow Junction, ST 00000
Ultimately we have the main business card with all doctor sames and that card has two versions  (front is always the same).  The back has two designs (1) displays next appointment time/date, (2) for "general use" (non-appointment.)    I have attached what we have used in the past.  
We also need a design template for each team member in our practice with their name, title, and email.   Those should be designed with the "general use" back (see attached).
**Open to entirely new design so don't feel obligated to keep current format.  Need new perspective!  Also including our watermark and some other design features we have consistently used in past in our portfolio.  Included are two options for logos--vertical and horizontal.
**I also would like to remove "Member of Sight Alliance" on our logo if possible**
 Other image files available upon request.

Target Market(s)

New patient & Current Patients

Industry/Entity Type

Optometry

Contact Information for Business Card

High-tech optometry practice with 3 doctors seeking new business card.  We provide eye exams, sell, designer glasses/contacts/specialty eyewear and treat ocular diseases.  For our business cards, we are seeking fresh, clean, and crisp design as we grow our team (staffing change).  Simply adding doctors is making the card look busy/cluttered.  Looking for professional, less cluttered look yet still have our logo, doctor names, phone, address, and website....If possible!  :) Names: Marcia Trelford, O.D. Ned Pallister, O.D. Oona Ferrant, O.D. Phone: 555-014-2738 Website: www.BrightLensHub.example Address:  417 Garnet R. Holloway, Harlow Junction, ST 00000 Ultimately we have the main business card with all doctor sames and that card has two versions  (front is always the same).  The back has two designs (1) displays next appointment time/date, (2) for "general use" (non-appointment.)    I have attached what we have used in the past.   We also need a design template for each team member in our practice with their name, title, and email.   Those should be designed with the "general use" back (see attached). **Open to entirely new design so don't feel obligated to keep current format.  Need new perspective!  Also including our watermark and some other design features we have consistently used in past in our portfolio.  Included are two options for logos--vertical and horizontal. **I also would like to remove "Member of Sight Alliance" on our logo if possible**  Other image files available upon request.

Font styles to use
Other font styles liked:
• We have used Montserrat / Yellowtail in the past

Colors

Designer to choose colors to be used in the design.

Requirements
Must have
• Clean & Fresh Design with Logo / Info provided in description. Horizontal orientation. **I have included the CMYK colors we currently have in our logo.
Should not have
• Cluttered

```html
<!DOCTYPE html>
<html lang="en">
<head>
<meta charset="utf-8">
<title>BrightLens Hub – Business Card Set</title>
<link href="https://fonts.googleapis.com/css2?family=Montserrat:wght@400;500;600;700&display=swap" rel="stylesheet">
<style>
  :root {
    --backdrop: #bfccd4;
    --card: #ffffff;
    --brand-blue: #2f5c85;
    --ink: #1f1f1f;
    --band-grey: #eeeff1;
    --divider: #8a8a8a;
    --band-dark: #231f20;
    --on-band: #ffffff;
  }
  * { box-sizing: border-box; margin: 0; padding: 0; }
  html, body { width: 1200px; height: 1200px; overflow: hidden; }
  body {
    background: var(--backdrop);
    font-family: "Montserrat", sans-serif;
    position: relative;
  }
  .card-sheet {
    position: absolute;
    left: 40px; top: 272px;
    display: grid;
    grid-template-columns: 540px 540px;
    grid-template-rows: 308px 308px;
    gap: 40px;
  }
  .card {
    position: relative;
    background: var(--card);
    overflow: hidden;
    box-shadow: 4px 5px 8px rgba(0,0,0,0.35);
    color: var(--brand-blue);
  }
  .icon { width: 12px; height: 12px; fill: currentColor; flex: none; }

  /* Front */
  .front .accent-bar {
    position: absolute; left: 0; top: 64px; width: 12px; height: 180px;
    background: var(--brand-blue);
  }
  .front .brand-mark {
    position: absolute; left: 66px; top: 20px; width: 66px; height: 66px;
    border-radius: 50%; background: var(--brand-blue);
  }
  .front .brand-name {
    position: absolute; left: 26px; top: 98px;
    font-size: 31px; font-weight: 400; line-height: 36px;
    color: var(--brand-blue);
  }
  .front .holder-name {
    position: absolute; left: 26px; top: 196px;
    font-size: 21px; font-weight: 700; letter-spacing: 1.5px; line-height: 22px;
  }
  .front .doctor-list {
    position: absolute; left: 282px; top: 102px;
    font-size: 17px; font-weight: 500; letter-spacing: 2.2px; line-height: 22px;
    list-style: none;
  }
  .front .doctor-list li { border-bottom: 1.5px solid var(--brand-blue); }
  .front .contact {
    position: absolute; left: 282px; top: 194px;
    font-size: 14px; font-weight: 500; letter-spacing: 1px; line-height: 19px;
  }
  .front .contact-row { display: flex; gap: 8px; align-items: flex-start; }
  .front .contact-row .icon { margin-top: 3px; width: 14px; height: 14px; }
  .links {
    position: absolute; left: 26px; right: 26px;
    display: flex; justify-content: space-between;
    font-size: 11px; font-weight: 500; letter-spacing: 0.5px;
  }
  .links span { display: flex; gap: 6px; align-items: center; }
  .front .links { top: 282px; }

  /* Appointment back */
  .back .brand-lockup {
    position: absolute; left: 0; right: 0; top: 22px;
    display: flex; justify-content: center; align-items: center; gap: 20px;
  }
  .back .brand-mark {
    width: 70px; height: 70px; border-radius: 50%; background: var(--brand-blue);
  }
  .back.dark .brand-mark { background: var(--band-dark); }
  .back .brand-name {
    font-size: 31px; font-weight: 400; line-height: 36px; color: var(--brand-blue);
  }
  .back .appointment-band {
    position: absolute; left: 0; right: 0; top: 118px; height: 44px;
    background: var(--band-grey);
    display: flex; justify-content: center; align-items: center;
    font-size: 16px; font-weight: 600; letter-spacing: 1.5px; color: var(--ink);
  }
  .back .appointment-fields {
    position: absolute; left: 0; right: 0; top: 162px; height: 58px;
    font-size: 16px; font-weight: 600; letter-spacing: 1.5px; color: var(--ink);
  }
  .back .field-date { position: absolute; left: 125px; top: 6px; }
  .back .field-time { position: absolute; left: 362px; top: 6px; }
  .back .field-divider {
    position: absolute; left: 270px; top: 0; width: 1.5px; height: 58px;
    background: var(--divider);
  }
  .back .notice-band {
    position: absolute; left: 0; right: 0; top: 220px; height: 88px;
    background: var(--brand-blue); color: var(--on-band);
  }
  .back.dark .notice-band { background: var(--band-dark); }
  .back .notice {
    position: absolute; left: 0; right: 0; top: 12px;
    text-align: center; font-size: 11.5px; font-weight: 600; letter-spacing: 1.2px; line-height: 14px;
  }
  .back .links { top: 60px; }
</style>
</head>
<body>
<svg width="0" height="0" style="position:absolute" aria-hidden="true">
  <symbol id="icon-phone" viewBox="0 0 24 24"><path d="M6.6 10.8a15 15 0 0 0 6.6 6.6l2.2-2.2a1 1 0 0 1 1-.25 11.4 11.4 0 0 0 3.6.57 1 1 0 0 1 1 1V20a1 1 0 0 1-1 1A17 17 0 0 1 3 4a1 1 0 0 1 1-1h3.5a1 1 0 0 1 1 1c0 1.25.2 2.450.57 3.57a1 1 0 0 1-.25 1z"/></symbol>
  <symbol id="icon-pin" viewBox="0 0 24 24"><path d="M12 2a7 7 0 0 0-7 7c0 5.2 7 13 7 13s7-7.8 7-13a7 7 0 0 0-7-7zm0 9.5A2.5 2.5 0 1 1 12 6.5a2.5 2.5 0 0 1 0 5z"/></symbol>
  <symbol id="icon-globe" viewBox="0 0 24 24"><path d="M12 2a10 10 0 1 0 0 20 10 10 0 0 0 0-20zm6.9 6h-2.9a15 15 0 0 0-1.4-3.6A8 8 0 0 1 18.9 8zM12 4a13 13 0 0 1 1.9 4h-3.8A13 13 0 0 1 12 4zM4.3 14a8 8 0 0 1 0-4h3.4a16 16 0 0 0 0 4zm.8 2h2.9a15 15 0 0 0 1.4 3.6A8 8 0 0 1 5.1 16zm2.9-8H5.1a8 8 0 0 1 4.3-3.6A15 15 0 0 0 8 8zm4 12a13 13 0 0 1-1.9-4h3.8A13 13 0 0 1 12 20zm2.3-6H9.7a14 14 0 0 1 0-4h4.6a14 14 0 0 1 0 4zm.3 5.6A15 15 0 0 0 16 16h2.9a8 8 0 0 1-4.3 3.6zm1.7-5.6a16 16 0 0 0 0-4h3.4a8 8 0 0 1 0 4z"/></symbol>
  <symbol id="icon-mail" viewBox="0 0 24 24"><path d="M2 5h20v14H2zm2 2v.4l8 5.3 8-5.3V7zm0 2.8V17h16V9.8l-8 5.3z"/></symbol>
</svg>

<main class="card-sheet">
  <section class="card front" aria-label="Card front">
    <div class="accent-bar"></div>
    <div class="brand-mark"></div>
    <p class="brand-name">BrightLens<br>Hub</p>
    <p class="holder-name">Marcia<br>Trelford, O.D.</p>
    <ul class="doctor-list">
      <li>O.D. Ned Pallister</li>
      <li>O.D. Oona Ferrant</li>
    </ul>
    <div class="contact">
      <div class="contact-row"><svg class="icon"><use href="#icon-phone"/></svg><span>555-014-2738</span></div>
      <div class="contact-row"><svg class="icon"><use href="#icon-pin"/></svg><span>417 Garnet R. Holloway,<br>Harlow Junction,<br>ST 00000</span></div>
    </div>
    <div class="links">
      <span><svg class="icon"><use href="#icon-globe"/></svg>www.BrightLensHub.example</span>
      <span><svg class="icon"><use href="#icon-mail"/></svg>MTrelford@brightlenshub.example</span>
    </div>
  </section>

  <section class="card front" aria-label="Card front, second version">
    <div class="accent-bar"></div>
    <div class="brand-mark"></div>
    <p class="brand-name">BrightLens<br>Hub</p>
    <p class="holder-name">Marcia<br>Trelford, O.D.</p>
    <ul class="doctor-list">
      <li>O.D. Ned Pallister</li>
      <li>O.D. Oona Ferrant</li>
    </ul>
    <div class="contact">
      <div class="contact-row"><svg class="icon"><use href="#icon-phone"/></svg><span>555-014-2738</span></div>
      <div class="contact-row"><svg class="icon"><use href="#icon-pin"/></svg><span>417 Garnet R. Holloway,<br>Harlow Junction,<br>ST 00000</span></div>
    </div>
    <div class="links">
      <span><svg class="icon"><use href="#icon-globe"/></svg>www.BrightLensHub.example</span>
      <span><svg class="icon"><use href="#icon-mail"/></svg>MTrelford@brightlenshub.example</span>
    </div>
  </section>

  <section class="card back" aria-label="Appointment card back, blue">
    <div class="brand-lockup">
      <div class="brand-mark"></div>
      <p class="brand-name">BrightLens<br>Hub</p>
    </div>
    <div class="appointment-band">Your Next Appointment</div>
    <div class="appointment-fields">
      <span class="field-date">Date:</span>
      <span class="field-divider"></span>
      <span class="field-time">Time</span>
    </div>
    <div class="notice-band">
      <p class="notice">If Your Unable To Keep Your Appointment,<br>Kindly Give Us 24 Hour Notice</p>
      <div class="links">
        <span><svg class="icon"><use href="#icon-globe"/></svg>www.BrightLensHub.example</span>
        <span><svg class="icon"><use href="#icon-mail"/></svg>MTrelford@brightlenshub.example</span>
      </div>
    </div>
  </section>

  <section class="card back dark" aria-label="Appointment card back, dark">
    <div class="brand-lockup">
      <div class="brand-mark"></div>
      <p class="brand-name">BrightLens<br>Hub</p>
    </div>
    <div class="appointment-band">Your Next Appointment</div>
    <div class="appointment-fields">
      <span class="field-date">Date:</span>
      <span class="field-divider"></span>
      <span class="field-time">Time</span>
    </div>
    <div class="notice-band">
      <p class="notice">If Your Unable To Keep Your Appointment,<br>Kindly Give Us 24 Hour Notice</p>
      <div class="links">
        <span><svg class="icon"><use href="#icon-globe"/></svg>www.BrightLensHub.example</span>
        <span><svg class="icon"><use href="#icon-mail"/></svg>MTrelford@brightlenshub.example</span>
      </div>
    </div>
  </section>
</main>
</body>
</html>
```